Book a Belle needs a Stunning web design

Book a Belle is an upmarket agency in Sydney that has lingerie waitresses for events.

Book a Belle is looking for a website design that is as sexy and sophisticated as the ladies who work for them!

The design mustn't be cluttered, tacky or pornographic. What I'm looking for is something better than the industry leader www.velvetgrace.com.au Something classy, sexy and different.

When designing please suggest a CMS, we already use wordpress but are open to suggestions.

We will need a home page that incorporates a feed from a blog and/or social media (please make suggestions and use your discretion as a designer, however we'd like to approve what goes into the feed before it goes in.) The home page could also have a list of our services, but if not we will need a services page. Our Services include:
Lingerie waitressing at events
Lingerie waitresses to help dress the groom pre wedding.
Bucks parties

We have a logo that we'd like incorporated into the design and have attached it.

We will also need a portfolio page for the ladies, This is not to be cluttered, tacky or pornographic. It needs to be classy.

We will also need a "Contact us" page and were thinking that this could potentially also be a "Ask for a quote on your event" page. I.e. have a regular "Contact us" form but have alternate fields if they tick the "I want a quote" box. Alternatively you could have two parts to the contact us page. One that is a regular form and one that has a "Your requirements" box.

Again please use your discretion when designing these, if it's too cluttered it won't work. If it looks tacky, don't do it. If you have suggestions make them.

Target Market(s)

Males between the ages of 18 - 45

Industry/Entity Type

Industry

Requirements
Must have
• Must incorporate our logo.

```html
<!DOCTYPE html>
<html lang="en">
<head>
<meta charset="utf-8">
<title>Book a Belle</title>
<link href="https://fonts.googleapis.com/css2?family=Oswald:wght@600&family=Roboto+Condensed:wght@700&family=Arimo:ital,wght@0,400;0,700;1,700&display=swap" rel="stylesheet">
<style>
:root{
  --bg:#151515;
  --bg-line:#1b1b1b;
  --red:#e0112c;
  --white:#ffffff;
  --grey:#8f8f8f;
  --grey-light:#bdbdbd;
  --panel:#222;
  --nav-top:#353535;
  --nav-bottom:#1c1c1c;
  --border:#3a3a3a;
}
*{margin:0;padding:0;box-sizing:border-box}
html,body{width:915px;height:1200px;overflow:hidden}
body{
  position:relative;
  background-color:var(--bg);
  background-image:repeating-linear-gradient(0deg,var(--bg-line) 0 1px,transparent 1px 3px),
                   repeating-linear-gradient(90deg,var(--bg-line) 0 1px,transparent 1px 3px);
  font-family:"Arimo",Arial,sans-serif;
  color:var(--white);
}
.abs{position:absolute}
.brand{left:86px;top:46px;display:flex;align-items:center;gap:10px}
.brand-name{font-family:"Arimo",sans-serif;font-weight:700;font-size:30px;color:var(--red);white-space:nowrap}
.brand-mark{width:14px;height:14px;border-radius:50%;background:var(--red)}
.account{left:618px;top:31px;display:flex;align-items:center;gap:8px;font-size:11px;color:var(--grey-light)}
.account .sep{color:var(--grey)}
.social{top:25px;width:24px;height:24px;border-radius:4px;background:#5a6f9a}
.social.one{left:825px}
.social.two{left:856px;background:#4aa8d8}
.search{left:664px;top:79px;width:161px;height:27px;border:1px solid #4a4a4a;background:#101010;font-size:11px;color:var(--grey);padding:7px 13px}
.go{left:834px;top:79px;width:45px;height:27px;background:var(--red);font-family:"Roboto Condensed",sans-serif;font-size:20px;line-height:27px;text-align:center;color:var(--white)}
.nav{left:36px;top:130px;width:843px;height:54px;background:linear-gradient(var(--nav-top),var(--nav-bottom));border-top:1px solid #444}
.nav a{position:absolute;top:18px;font-size:14px;letter-spacing:1px;color:var(--white);text-decoration:none}
.nav a.active{color:var(--red)}
.hero-photo{left:492px;top:193px;width:388px;height:877px;background:radial-gradient(ellipse at 50% 40%,#bdbcc2,#8a8890 70%,#6f6d75)}
.hero-title{left:91px;top:218px;font-family:"Oswald",sans-serif;font-weight:600;font-size:74px;line-height:1;color:var(--red);letter-spacing:1px}
.hero-sub{left:93px;top:286px;font-weight:700;font-style:italic;font-size:28px;color:#9a9a9a;letter-spacing:1px}
.hero-text{left:93px;top:353px;width:340px;font-size:14px;line-height:19px;color:var(--grey)}
.btn-main{left:94px;top:430px;width:197px;height:39px;background:#2c2c2c;border:1px solid #3a3a3a;display:flex;align-items:center;padding-left:23px;gap:20px;font-weight:700;font-size:19px}
.dots{left:94px;top:527px;display:flex;gap:6px}
.dots span{width:18px;height:18px;border-radius:50%;background:radial-gradient(circle at 40% 35%,#777,#3a3a3a)}
.dots span.on{background:radial-gradient(circle at 40% 35%,#ff4a5c,#c00a20)}
.feed{left:36px;top:604px;width:431px;height:466px;border:1px solid var(--border)}
.post{position:absolute;left:60px;width:360px}
.post h2{font-family:"Roboto Condensed",sans-serif;font-weight:700;font-size:21px;color:var(--red);letter-spacing:.5px}
.post .thumb{position:absolute;left:0;top:36px;width:108px;height:108px;border:1px solid #555;background:linear-gradient(#58566a,#2e2c38)}
.post h3{position:absolute;left:122px;top:40px;font-family:"Roboto Condensed",sans-serif;font-weight:700;font-size:14px;letter-spacing:.8px}
.post p{position:absolute;left:122px;top:72px;width:240px;font-size:11px;line-height:17px}
.btn-small{position:absolute;left:123px;top:145px;width:99px;height:21px;background:#2c2c2c;border:1px solid #3a3a3a;display:flex;align-items:center;padding-left:11px;gap:10px;font-weight:700;font-size:9px}
.footer{left:36px;top:1096px;width:843px;height:85px;background:var(--panel)}
.footer-text{position:absolute;left:21px;top:15px;width:600px;font-size:11px;line-height:15px}
.footer-links{position:absolute;left:21px;top:56px;font-size:12px;font-weight:700;color:var(--red)}
.footer-links span{color:var(--red);margin:0 6px}
.legal{position:absolute;left:653px;top:15px;font-size:11px;line-height:15px;list-style:none}
.legal li::before{content:"▸ ";font-size:8px}
</style>
</head>
<body>
<header>
  <div class="abs brand"><span class="brand-name">Book a Belle</span><span class="brand-mark"></span></div>
  <div class="abs account">
    <svg width="20" height="18" viewBox="0 0 20 18"><circle cx="10" cy="5" r="5" fill="#8f8f8f"/><path d="M0 18c0-6 4-8 10-8s10 2 10 8z" fill="#8f8f8f"/></svg>
    <span>My Account</span><span class="sep">|</span><span>Login or Register</span>
  </div>
  <div class="abs social one"></div>
  <div class="abs social two"></div>
  <div class="abs search">Search girls</div>
  <div class="abs go">GO</div>
  <nav class="abs nav">
    <a class="active" style="left:57px">HOME</a>
    <a style="left:136px">SEMPER</a>
    <a style="left:234px">NUSQUAM</a>
    <a style="left:343px">LEGERE</a>
    <a style="left:438px">ELECTRAM</a>
    <a style="left:554px">OMNIUS REBUS</a>
    <a style="left:702px">CONTACT</a>
  </nav>
</header>

<main>
  <div class="abs hero-title">CAUSA</div>
  <div class="abs hero-sub">PRINCIPES</div>
  <p class="abs hero-text">SOLET IUVARET IUDICABIT NEC EA, NE HAS ENIM PROPRIAE. EX NEC MAZIM IMPERDIET, DECORE</p>
  <div class="abs btn-main">READ MORE
    <svg width="32" height="32" viewBox="0 0 32 32"><circle cx="16" cy="16" r="15" fill="#fff"/><path d="M8 14h9v-5l8 7-8 7v-5H8z" fill="#2c2c2c"/></svg>
  </div>
  <div class="abs dots"><span></span><span class="on"></span><span></span><span></span></div>

  <div class="abs hero-photo" role="img" aria-label="Photo of two models in black lingerie and heels against a grey studio backdrop"></div>

  <section class="abs feed">
    <article class="post" style="top:44px">
      <h2>Solet iuvaret iudicabit</h2>
      <div class="thumb" role="img" aria-label="Portrait photo of a model"></div>
      <h3>Solet iuvaret iudicabit nec</h3>
      <p>Solet iuvaret iudicabit nec ea, ne has enim propriae. Ex nec mazim imperdiet, decore nullam repudiandae ut ius. Elitr tation quo</p>
      <div class="btn-small">READ MORE
        <svg width="16" height="16" viewBox="0 0 32 32"><circle cx="16" cy="16" r="15" fill="#fff"/><path d="M8 14h9v-5l8 7-8 7v-5H8z" fill="#2c2c2c"/></svg>
      </div>
    </article>
    <article class="post" style="top:256px">
      <h2>Solet iuvaret iudicabit</h2>
      <div class="thumb" role="img" aria-label="Portrait photo of a model"></div>
      <h3>Solet iuvaret iudicabit nec</h3>
      <p>Solet iuvaret iudicabit nec ea, ne has enim propriae. Ex nec mazim imperdiet, decore nullam repudiandae ut ius. Elitr tation quo</p>
      <div class="btn-small">READ MORE
        <svg width="16" height="16" viewBox="0 0 32 32"><circle cx="16" cy="16" r="15" fill="#fff"/><path d="M8 14h9v-5l8 7-8 7v-5H8z" fill="#2c2c2c"/></svg>
      </div>
    </article>
  </section>
</main>

<footer class="abs footer">
  <p class="footer-text">Usu vide iudicabit ex. Libris voluptua vix in, falli nobis necessitatibus per ut. An sit vidit invidunt definiebas, eum quas tacimates assueverit ex. Ut magna velit iracundia mea, ei reque homero principes duo.</p>
  <div class="footer-links">Libris<span>|</span>Legimus<span>|</span>Efficiantur<span>|</span>Feugiat<span>|</span>Tractatos<span>€</span>Corpora<span>|</span>Forensibus<span>|</span>Propriae</div>
  <ul class="legal"><li>Terms and Conditions</li><li>Privacy Policy</li></ul>
</footer>
</body>
</html>
```